Resinex Pro color chart design

We are in need to have a color chart (pdf to be displayed on our website-www.resinexpro-sample.com as well as for print) to show customers what their color choices are for our metallic epoxy pigments. We would like it to be modern amd clean. A white background will allow the color swatches to stand out. our company colors are orange, grey and white. Looking for the color swatches to be as large as possible while still being able to display our logo, contact info and disclaimers. We are open to any design ideas. If needed it can be put on two pages.

Additional info to add: Resinex Pro Shimmer Tint Powders are special effect pigments composed of mica nano-particles coated with various organic and inorganic pigments to create pearlescent and iridescent effects that mimic the
natural look of stone and rock formations. These unique pigments are designed to be field blended with Resinex Pro Artisan Lustre clear epoxy. When the metallic particles are mixed with our epoxy they give the coating a shine that reflects light and creates an eye-catching dramatic color. For the most vivid color and dynamic effects we recommend (1) 16oz jar of metallic pigment for each 3 Gallon kit of our Artisan Lustre Epoxy.

Disclaimer: The colors on this chart are represented as closely as possible. Variations should be expected due to differences in substrate conditions, thickness of application, speed of curing, blending of colors, application technique, color of initial primer coat and screen resolution. For additional information and application instructions visit www.resinexpro-sample.com

Contact info: Tel. 1-800-555-0147
www.resinexpro-sample.com

Target Market(s)

Online. This will be a link on our website

Font styles to use
Sans Serif

Colors
f37122
5c5c5c
ffffff

Requirements
Must have
• A white background will allow the color swatches to stand out. Disclaimer should be in small print but still readable.
Nice to have
• Can use our company colors as part of the design
Should not have
• Should not look and feel cluttered.

```html
<!DOCTYPE html>
<html lang="en">
<head>
<meta charset="utf-8">
<title>Resinex Pro – Metallics Color Chart</title>
<link rel="stylesheet" href="https://fonts.googleapis.com/css2?family=Open+Sans:wght@300;400;700&family=Roboto+Condensed:wght@700&display=swap">
<style>
  :root {
    --brand-orange: #f37122;
    --brand-grey: #5c5c5c;
    --band-grey: #4b4b4b;
    --white: #ffffff;
    --label: #2b2b2b;
    --fine-print: #d8d8d8;
  }
  html, body { margin: 0; padding: 0; overflow: hidden; }
  body { width: 900px; height: 1200px; background: var(--white); font-family: "Open Sans", sans-serif; }
  .chart { position: relative; width: 900px; height: 1200px; display: flex; flex-direction: column; }

  .chart-header {
    height: 80px; flex: none; background: linear-gradient(180deg, #555 0%, var(--band-grey) 100%);
    display: flex; align-items: center; justify-content: space-between; padding: 0 40px 0 26px;
  }
  .brand-name { color: var(--white); font-weight: 700; font-size: 30px; line-height: 1; }
  .brand-line { color: var(--fine-print); font-size: 11px; margin-top: 4px; }
  .chart-title { color: var(--white); font-weight: 300; font-size: 52px; letter-spacing: 1px; margin: 0; }

  .swatch-grid {
    flex: 1; display: grid; grid-template-columns: repeat(4, 1fr); grid-template-rows: repeat(6, 1fr);
    padding: 10px 40px 4px; list-style: none; margin: 0;
  }
  .swatch { display: flex; flex-direction: column; align-items: center; justify-content: center; }
  .swatch-chip {
    width: 134px; height: 134px; border-radius: 50%;
    background:
      radial-gradient(circle at 35% 30%, rgba(255,255,255,0.28) 0%, rgba(255,255,255,0) 55%),
      radial-gradient(circle at 60% 75%, rgba(0,0,0,0.18) 0%, rgba(0,0,0,0) 60%),
      var(--chip);
  }
  .swatch-name {
    margin-top: 6px; font-family: "Roboto Condensed", sans-serif; font-weight: 700;
    font-size: 14px; line-height: 17px; color: var(--label); text-transform: uppercase; letter-spacing: 0.3px;
  }

  .chart-footer {
    height: 140px; flex: none; background: linear-gradient(180deg, var(--band-grey) 0%, #3f3f3f 100%);
    padding: 16px 24px 0; box-sizing: border-box; text-align: center;
  }
  .disclaimer { color: var(--fine-print); font-size: 11.5px; line-height: 1.55; margin: 0 0 20px; text-align: left; }
  .disclaimer strong { color: var(--white); }
  .contact { color: var(--brand-orange); font-weight: 700; font-size: 20px; margin: 0; letter-spacing: 0.5px; }
  .contact .sep { margin: 0 14px; letter-spacing: 6px; }
</style>
</head>
<body>
<div class="chart">
  <header class="chart-header">
    <div class="brand">
      <div class="brand-name">Resinex Pro</div>
      <div class="brand-line">Shimmer Tint Powders</div>
    </div>
    <h1 class="chart-title">Metallics</h1>
  </header>

  <ul class="swatch-grid">
    <li class="swatch"><span class="swatch-chip" style="--chip:#b8701c"></span><span class="swatch-name">Brass</span></li>
    <li class="swatch"><span class="swatch-chip" style="--chip:#a4461c"></span><span class="swatch-name">Bubblegum</span></li>
    <li class="swatch"><span class="swatch-chip" style="--chip:#a34816"></span><span class="swatch-name">Cairo</span></li>
    <li class="swatch"><span class="swatch-chip" style="--chip:#f1b416"></span><span class="swatch-name">Canary</span></li>
    <li class="swatch"><span class="swatch-chip" style="--chip:#8a3812"></span><span class="swatch-name">Cinnamon</span></li>
    <li class="swatch"><span class="swatch-chip" style="--chip:#3a2216"></span><span class="swatch-name">Coffee</span></li>
    <li class="swatch"><span class="swatch-chip" style="--chip:#a8421a"></span><span class="swatch-name">Copper</span></li>
    <li class="swatch"><span class="swatch-chip" style="--chip:#c9c9cc"></span><span class="swatch-name">Diamond</span></li>
    <li class="swatch"><span class="swatch-chip" style="--chip:#1e4a35"></span><span class="swatch-name">Forest Green</span></li>
    <li class="swatch"><span class="swatch-chip" style="--chip:#3b1a7c"></span><span class="swatch-name">Grape</span></li>
    <li class="swatch"><span class="swatch-chip" style="--chip:#2b5a33"></span><span class="swatch-name">Green Apple</span></li>
    <li class="swatch"><span class="swatch-chip" style="--chip:#1c1c1e"></span><span class="swatch-name">Gunmetal</span></li>
    <li class="swatch"><span class="swatch-chip" style="--chip:#7b3fa0"></span><span class="swatch-name">Lilac</span></li>
    <li class="swatch"><span class="swatch-chip" style="--chip:#1b4c9c"></span><span class="swatch-name">Ocean Blue</span></li>
    <li class="swatch"><span class="swatch-chip" style="--chip:#a89418"></span><span class="swatch-name">Olive Yellow</span></li>
    <li class="swatch"><span class="swatch-chip" style="--chip:#d97816"></span><span class="swatch-name">Orange Gold</span></li>
    <li class="swatch"><span class="swatch-chip" style="--chip:#ede1dc"></span><span class="swatch-name">Pearl</span></li>
    <li class="swatch"><span class="swatch-chip" style="--chip:#7a3010"></span><span class="swatch-name">Penny</span></li>
    <li class="swatch"><span class="swatch-chip" style="--chip:#119a80"></span><span class="swatch-name">Sea Green</span></li>
    <li class="swatch"><span class="swatch-chip" style="--chip:#9d9da1"></span><span class="swatch-name">Silver</span></li>
    <li class="swatch"><span class="swatch-chip" style="--chip:#1a7ba8"></span><span class="swatch-name">Sky Blue</span></li>
    <li class="swatch"><span class="swatch-chip" style="--chip:#f76a10"></span><span class="swatch-name">Tangerine</span></li>
    <li class="swatch"><span class="swatch-chip" style="--chip:#5a5a5e"></span><span class="swatch-name">Titanium</span></li>
    <li class="swatch"><span class="swatch-chip" style="--chip:#7a1010"></span><span class="swatch-name">Wine Red</span></li>
  </ul>

  <footer class="chart-footer">
    <p class="disclaimer"><strong>Disclaimer:</strong> The colors on this chart are represented as closely as possible. Variations should be expected due to differences in substrate conditions, thickness of application, speed of curing, blending of colors, application technique, color of initial primer coat and screen resolution. For additional information and application instructions visit www.resinexpro-sample.com</p>
    <p class="contact">1-800-555-0147<span class="sep">•••</span>www.resinexpro-sample.com</p>
  </footer>
</div>
</body>
</html>
```